Webbanner für Verkauf von Pools und Poolzubehör gesucht
Zielgruppe
Wir verkaufen Pools und Poolzubehör mit einer top Beratung zum fairen Preis.
Aufgabenstellung
Wir möchten ein Webbanner wie es bereits auf unserer Website auf der Startseite als Slider eingebaut ist (vom Format).
Es sollte wie das Bild unten sein, aber auf unsere Branche umgebaut werden (also ein total zerstörter Pool zum Beispiel oder eine üble Baustelle o. ä.)
Der Text wie im Bild unten und dann ergänzt zum Beispiel mit:
Möchten Sie das?
Bei uns gibt es Top-Beratung und hochwertige Ware zum fairen Preis.
Der Text kann auch ähnlich sein. Die Aussage, die dahinter steckt, ist wichtig.
Der Banner soll später auch in die Mails zu unserern Angeboten mit eingebaut werden.

```html
<!DOCTYPE html>
<html lang="de">
<head>
<meta charset="utf-8">
<title>Aquaruh24 – Pool &amp; Zubehör</title>
<link rel="stylesheet" href="https://fonts.googleapis.com/css2?family=Open+Sans:wght@400;600;700&display=swap">
<style>
:root{
  --water:#2aa8cf;
  --water-dark:#1480a8;
  --page:#ffffff;
  --line:#dcdcdc;
  --text:#333333;
  --nav-text:#555555;
  --brand:#1aa3dc;
  --cyan:#2bb9e4;
  --blue:#2f8fdc;
  --accent:#29b3e6;
}
*{margin:0;padding:0;box-sizing:border-box}
html,body{width:1200px;height:944px;overflow:hidden}
body{font-family:"Open Sans",sans-serif;color:var(--text);position:relative;background:var(--page)}
.water{position:absolute;top:0;width:18px;height:944px;background:linear-gradient(160deg,var(--water) 0%,var(--water-dark) 50%,var(--water) 100%)}
.water.left{left:0}
.water.right{right:0;width:26px}
.page{position:absolute;left:18px;top:0;width:1156px;height:944px;background:var(--page)}
.logo{position:absolute;left:25px;top:12px;display:flex;align-items:center;gap:8px}
.logo .dot{width:16px;height:16px;border-radius:50%;background:var(--brand)}
.logo .name{font-size:30px;font-weight:700;color:var(--brand);letter-spacing:-.5px}
.search{position:absolute;left:644px;top:4px;width:243px;height:33px;border:1px solid #ccc;border-radius:3px;display:flex}
.search .field{flex:1;padding:6px 12px;font-size:14px;color:#999}
.search .btn{width:42px;border-left:1px solid #ccc;background:#f3f3f3;display:flex;align-items:center;justify-content:center}
.account,.cart{position:absolute;top:12px;font-size:15px;color:var(--text);display:flex;align-items:center;gap:4px}
.account{left:918px}
.cart{left:1045px}
.caret{width:0;height:0;border-left:4px solid transparent;border-right:4px solid transparent;border-top:4px solid #333;margin-left:4px}
.navbar{position:absolute;left:0;top:100px;width:1156px;height:52px;border-top:2px solid var(--line);border-bottom:2px solid var(--line)}
.navbar ul{list-style:none}
.navbar li{position:absolute;top:14px;font-size:15px;color:var(--nav-text);display:flex;align-items:center}
.navbar .caret{border-top-color:var(--nav-text)}
.slider{position:absolute;left:20px;top:177px;width:1114px;height:367px;overflow:hidden;box-shadow:0 4px 8px rgba(0,0,0,.15)}
.slider svg{position:absolute;left:0;top:0}
.headline{position:absolute;color:#fff;font-weight:700;white-space:nowrap}
.h1{left:63px;top:218px;font-size:31px}
.h2{left:92px;top:290px;font-size:26px}
.claim{position:absolute;left:548px;top:259px;font-size:17.5px;font-weight:600;line-height:25px;color:#222}
.claim em{font-style:normal;color:var(--accent)}
.banner-brand{position:absolute;left:903px;top:280px;display:flex;align-items:center;gap:6px}
.banner-brand .dot{width:12px;height:12px;border-radius:50%;background:var(--brand)}
.banner-brand .name{font-size:22px;font-weight:700;color:var(--brand)}
.dots{position:absolute;top:578px;left:520px;display:flex;gap:18px;align-items:center}
.dots span{width:6px;height:6px;border-radius:50%;background:#333}
.dots .on{width:11px;height:11px;border:2px solid #333;background:#fff}
.rule{position:absolute;left:26px;top:637px;width:1104px;height:1px;background:var(--line)}
.section-title{position:absolute;left:26px;top:655px;font-size:24px;font-weight:400;color:var(--text)}
.category{position:absolute;width:304px}
</style>
</head>
<body>
<div class="water left" role="img" aria-label="Wasseroberfläche im Pool"></div>
<div class="water right" role="img" aria-label="Wasseroberfläche im Pool"></div>
<div class="page">
  <header>
    <div class="logo"><span class="dot"></span><span class="name">Aquaruh24</span></div>
    <div class="search"><div class="field">Suchen</div><div class="btn">
      <svg width="18" height="18" viewBox="0 0 18 18"><circle cx="7.5" cy="7.5" r="5.5" fill="none" stroke="#1aa3dc" stroke-width="2.4"/><line x1="11.5" y1="11.5" x2="16" y2="16" stroke="#1aa3dc" stroke-width="2.6" stroke-linecap="round"/></svg>
    </div></div>
    <div class="account"><svg width="12" height="13" viewBox="0 0 12 13"><circle cx="6" cy="3.5" r="3" fill="#333"/><path d="M0 13c0-4 2.5-6 6-6s6 2 6 6z" fill="#333"/></svg>Anmelden<span class="caret"></span></div>
    <div class="cart"><svg width="14" height="12" viewBox="0 0 14 12"><path d="M0 1h2.5l2 7h7l2-5H4" fill="none" stroke="#333" stroke-width="1.8"/><circle cx="5.5" cy="10.5" r="1.3" fill="#333"/><circle cx="10.5" cy="10.5" r="1.3" fill="#333"/></svg>0,00 €<span class="caret"></span></div>
  </header>
  <nav class="navbar"><ul>
    <li style="left:27px">Pool &amp; Zubehör<span class="caret"></span></li>
    <li style="left:165px">Sauna<span class="caret"></span></li>
    <li style="left:241px">Infrarot<span class="caret"></span></li>
    <li style="left:325px">Holzbadewannen</li>
  </ul></nav>

  <section class="slider">
    <svg width="1114" height="367" viewBox="0 0 1114 367">
      <defs>
        <linearGradient id="poolScene" x1="0" y1="0" x2="1" y2="1">
          <stop offset="0" stop-color="#d9c3b6"/><stop offset=".45" stop-color="#7fd3e0"/><stop offset="1" stop-color="#c9a898"/>
        </linearGradient>
        <linearGradient id="siteScene" x1="0" y1="0" x2="0" y2="1">
          <stop offset="0" stop-color="#7ea858"/><stop offset=".45" stop-color="#6b6a55"/><stop offset="1" stop-color="#8a6e52"/>
        </linearGradient>
      </defs>
      <rect width="1114" height="367" fill="url(#poolScene)" role="img" aria-label="Fertiger Pool mit klarem Wasser im Garten"/>
      <polygon points="800,0 1114,0 1114,367 420,367" fill="url(#siteScene)" role="img" aria-label="Poolbaustelle mit Bewehrungsgittern und Holzschalung"/>
      <polygon points="505,241 1093,241 1073,334 485,334" fill="#fff"/>
      <polygon points="18,214 452,214 434,278 0,278" fill="var(--cyan)"/>
      <polygon points="58,278 523,278 503,343 38,343" fill="var(--blue)"/>
    </svg>
    <div class="headline h1">Bauen Sie einen Pool?</div>
    <div class="headline h2">Brauchen Sie Pool-Ausrüstung?</div>
    <p class="claim">Bei uns gibt es <em>Top-Beratung</em> und<br>hochwertige Ware zum <em>fairen Preis</em>.</p>
    <div class="banner-brand"><span class="dot"></span><span class="name">Aquaruh24</span></div>
  </section>

  <div class="dots"><span class="on"></span><span></span><span></span><span></span><span></span></div>
  <div class="rule"></div>
  <h2 class="section-title">Unsere TOP-Kategorien</h2>

  <div class="category" style="left:47px;top:769px;height:175px;background:linear-gradient(180deg,#9cc3e0 0%,#4f7a3c 45%,#b08a5a 100%)" role="img" aria-label="Achteckiger Holzpool im Garten"></div>
  <div class="category" style="left:426px;top:769px;height:175px;background:linear-gradient(90deg,#8c8c8c 0%,#1e9de8 30%,#1e9de8 70%,#8c8c8c 100%)" role="img" aria-label="Pool mit blauer Sicherheitsabdeckung"></div>
  <div class="category" style="left:804px;top:739px;height:205px;background:linear-gradient(180deg,#3f5a32 0%,#a9c6d8 50%,#8f9aa3 100%)" role="img" aria-label="Pool mit Rollladenabdeckung"></div>
</div>
</body>
</html>
```